Business card design for Velvet Harbor

We need business cards designed for our new marketing consulting company, Velvet Harbor. Our services include marketing strategy, go-to-market and launch planning, growth strategy, and execution. We serve medical technology and health technology companies, from startups to well-established growth companies.

The business cards should feel professional, credible, reliable and trustworthy, and should instill confidence. Also bold, creative, and modern.

The design must use the Velvet Harbor logo.

The primary brand color is this orange: #FF5501
A secondary color that you can use is this gray: #282B2D
I would prefer only to use the orange and gray. But if you feel you really need an additional accent color (please use it very sparingly, as little as possible), you can use this blue for small accent purposes: #009FED

Attached are the logo files. The main logo is the one with a little bit of orange on the left and the rest is gray.

The business card should include the following:

Velvet Harbor logo
First name and last name
Title
Email address
Phone number and type (in whatever order looks best for the design
Website (the website does not need to be in the same block as the personal info)

For example:

Nessa Pryle
Founder & Principal
nessa@velvetharbor.com
+1.628.309.4156 mobile (can use "." or spaces in between blocks of numbers)
velvetharbor.com (somewhere on the card, it does not need to be with the personal info; and note that there is no "www." at the beginning)

Note that there will be no address listed on the business card.

Target Market(s)

Executives (CEO, head of marketing, head of sales) at medical technology and health technology companies, mostly in their 40s and older, well-educated, often with advanced degrees. They are strategic thinkers, responsible for budgets, and familiar with P&L. Their comfort with and trust in using outside consultants varies.

Industry/Entity Type

Medical technology and health technology companies.

Contact Information for Business Card

See project description

Font styles to use
Sans Serif

Requirements
Must have
• Logo and see Business card details section above.

```html
<!DOCTYPE html>
<html lang="en">
<head>
<meta charset="utf-8">
<title>Velvet Harbor — Business Card</title>
<link href="https://fonts.googleapis.com/css2?family=Barlow:wght@400;500;600;700&display=swap" rel="stylesheet">
<style>
  :root {
    --orange: #FF5501;
    --charcoal: #282B2D;
    --silver: #B6B9BC;
    --silver-light: #F4F4F5;
    --label: #7A7A7A;
    --white: #FFFFFF;
  }
  * { margin: 0; padding: 0; box-sizing: border-box; }
  html, body { width: 1200px; height: 1000px; overflow: hidden; background: var(--white); }
  body { position: relative; font-family: "Barlow", sans-serif; color: var(--charcoal); }

  .card { position: absolute; left: 282px; width: 638px; height: 364px; overflow: hidden; }
  .card--front {
    top: 94px;
    background: radial-gradient(circle at 190px 180px, var(--silver-light) 0, #DADBDD 120px, var(--silver) 300px, var(--silver) 100%);
  }
  .card--back {
    top: 550px;
    background: radial-gradient(circle at 460px 170px, #55575A 0, #3A3C3F 170px, var(--charcoal) 300px, var(--charcoal) 100%);
  }

  .side-label { position: absolute; left: 0; width: 1200px; text-align: center; font-size: 15px; color: var(--label); letter-spacing: 0.02em; }
  .side-label--front { top: 483px; }
  .side-label--back { top: 943px; }

  .brand { position: absolute; display: flex; align-items: center; }
  .brand__dot { border-radius: 50%; background: var(--orange); flex: none; }
  .brand__name { text-transform: uppercase; font-weight: 600; line-height: 1.05; letter-spacing: 0.22em; }

  .card--front .brand { left: 282px; top: 52px; gap: 20px; }
  .card--front .brand__dot { width: 30px; height: 30px; }
  .card--front .brand__name { font-size: 29px; color: var(--charcoal); }

  .card--back .brand { left: 104px; top: 138px; gap: 28px; }
  .card--back .brand__dot { width: 44px; height: 44px; }
  .card--back .brand__name { font-size: 40px; color: var(--white); }

  .person { position: absolute; left: 82px; top: 154px; }
  .person__name { font-size: 29px; font-weight: 700; line-height: 1.1; }
  .person__title { font-size: 21px; font-weight: 600; margin-top: 6px; }

  .contact { position: absolute; left: 334px; top: 250px; list-style: none; }
  .contact__item { display: flex; align-items: center; gap: 10px; font-size: 19px; line-height: 24px; color: var(--charcoal); }
  .contact__icon { width: 14px; height: 14px; fill: var(--orange); flex: none; }
</style>
</head>
<body>

<section class="card card--front" aria-label="Business card front">
  <div class="brand">
    <span class="brand__dot"></span>
    <span class="brand__name">Velvet<br>Harbor</span>
  </div>

  <div class="person">
    <h1 class="person__name">Nessa Pryle</h1>
    <p class="person__title">Founder &amp; Principal</p>
  </div>

  <ul class="contact">
    <li class="contact__item">
      <svg class="contact__icon" viewBox="0 0 14 14" aria-hidden="true"><path d="M1 3h12v8H1z"/><path d="M1 3l6 4.5L13 3" fill="none" stroke="#B6B9BC" stroke-width="1.2"/></svg>
      nessa@velvetharbor.com
    </li>
    <li class="contact__item">
      <svg class="contact__icon" viewBox="0 0 14 14" aria-hidden="true"><path d="M3 1l2.4 2.6-1.2 1.8c.8 1.8 2.3 3.3 4.3 4.3l1.8-1.2L13 11l-1.6 2C6 13 1 8 1 2.6z"/></svg>
      +1.628.309.4156
    </li>
    <li class="contact__item">
      <svg class="contact__icon" viewBox="0 0 14 14" aria-hidden="true"><g fill="none" stroke="#FF5501" stroke-width="1.3"><circle cx="7" cy="7" r="5.8"/><ellipse cx="7" cy="7" rx="2.5" ry="5.8"/><path d="M1.2 7h11.6"/></g></svg>
      velvetharbor.com
    </li>
  </ul>
</section>
<p class="side-label side-label--front">Front Side</p>

<section class="card card--back" aria-label="Business card back">
  <div class="brand">
    <span class="brand__dot"></span>
    <span class="brand__name">Velvet<br>Harbor</span>
  </div>
</section>
<p class="side-label side-label--back">Back Side</p>

</body>
</html>
```